Rollin’ Kites Copper Tide beer can design

We are not looking for a new logo, we want to use our current logo!! Current Logo is Attached. We want to incorporate our current logo into a full can design for our new non-alcoholic, THC infused Beer design. We cannot use animals or cartoons. We also can not say beer. We would like to use our main label found at www.rollinkites-example.com
Several ideas include having small images of beer cans and beer mugs all over the can as a background. Another idea is to make it freedom and liberty themed. We want to make sure people understand it is a beer, even though we can say beer on the can.

Target Market(s)

30-50 year olds

Industry/Entity Type

THC beverage

Logo Text

Rollin’ Kites Copper Tide

Colors
59FF00
82FF00
B8FF75
E3FFCB
F4FFEA

Requirements
Must have
• Full 12 oz beer can design
Should not have
• No word beer, do not need a new logo, need a can design

```html
<!DOCTYPE html>
<html lang="en">
<head>
<meta charset="utf-8">
<title>Rollin’ Kites Copper Tide – Can Label</title>
<link rel="stylesheet" href="https://fonts.googleapis.com/css2?family=Oswald:wght@500;700&display=swap">
<style>
  :root {
    --lime: #aaff00;
    --leaf-deep: #3d8f2a;
    --leaf-mid: #7cbf1e;
    --leaf-glow: #e6f500;
    --forest: #0b4a1f;
    --gold-light: #f6dcae;
    --gold-mid: #e8b77a;
    --copper: #c98a45;
    --cream: #ffffff;
  }
  html, body {
    margin: 0;
    padding: 0;
    width: 686px;
    height: 1200px;
    overflow: hidden;
    background: var(--lime);
  }
  .can-label {
    display: block;
    width: 686px;
    height: 1200px;
  }
  .brand-name {
    font-family: "Oswald", sans-serif;
    font-weight: 700;
    fill: var(--forest);
  }
  .thc-tag {
    font-family: "Oswald", sans-serif;
    font-weight: 700;
    fill: var(--gold-light);
    letter-spacing: 6px;
  }
  .product-title {
    font-family: "Oswald", sans-serif;
    font-weight: 700;
    fill: var(--forest);
  }
  .product-note {
    font-family: "Oswald", sans-serif;
    font-weight: 500;
    fill: var(--forest);
    letter-spacing: 9px;
  }
  .volume {
    font-family: "Oswald", sans-serif;
    font-weight: 700;
    fill: var(--forest);
  }
</style>
</head>
<body>
<svg class="can-label" viewBox="0 0 686 1200" xmlns="http://www.w3.org/2000/svg">
  <defs>
    <radialGradient id="fieldGlow" cx="0.55" cy="0.52" r="0.75">
      <stop offset="0" stop-color="var(--leaf-glow)"/>
      <stop offset="0.45" stop-color="var(--leaf-mid)"/>
      <stop offset="1" stop-color="var(--leaf-deep)"/>
    </radialGradient>
    <linearGradient id="goldBand" x1="0" y1="0" x2="0" y2="1">
      <stop offset="0" stop-color="var(--gold-mid)"/>
      <stop offset="0.45" stop-color="#fff7ea"/>
      <stop offset="1" stop-color="var(--copper)"/>
    </linearGradient>
    <linearGradient id="volumeBadge" x1="0" y1="0" x2="0" y2="1">
      <stop offset="0" stop-color="#fff3e0"/>
      <stop offset="0.5" stop-color="var(--gold-mid)"/>
      <stop offset="1" stop-color="var(--copper)"/>
    </linearGradient>
  </defs>

  <!-- Background field with scattered icon pattern -->
  <rect class="pattern-field" x="0" y="0" width="686" height="1200" fill="url(#fieldGlow)"
        role="img" aria-label="Repeating pattern of small leaves, hop cones and stemmed glasses in yellow"/>

  <!-- Gold band with arch -->
  <g class="crest-band">
    <path d="M0 335 H118 A225 225 0 0 1 568 335 H686 V560 H0 Z" fill="var(--forest)"/>
    <path d="M0 343 H126 A217 217 0 0 1 560 343 H686 V552 H0 Z" fill="url(#goldBand)"/>
    <path d="M143 560 A200 48 0 0 0 543 560 Z" fill="var(--forest)"/>
    <path d="M151 560 A192 40 0 0 0 535 560 Z" fill="var(--copper)"/>
  </g>

  <!-- Brand mark area -->
  <g class="brand-mark">
    <circle cx="343" cy="345" r="185" fill="var(--cream)" stroke="var(--forest)" stroke-width="8"/>
    <text class="brand-name" x="343" y="366" font-size="58" text-anchor="middle" textLength="290" lengthAdjust="spacingAndGlyphs">ROLLIN’ KITES</text>
  </g>

  <!-- THC tag -->
  <g class="thc-tag-group">
    <rect x="285" y="658" width="116" height="40" rx="20" fill="var(--forest)"/>
    <text class="thc-tag" x="346" y="692" font-size="32" text-anchor="middle">THC</text>
  </g>

  <!-- Title rules and stars -->
  <g class="title-rules" fill="var(--forest)">
    <rect x="0" y="760" width="162" height="22"/>
    <rect x="524" y="760" width="162" height="22"/>
    <rect x="0" y="858" width="196" height="22"/>
    <rect x="490" y="858" width="196" height="22"/>
    <polygon points="125,803 131,819 148,819 134,829 139,846 125,836 111,846 116,829 102,819 119,819"/>
    <polygon points="564,803 570,819 587,819 573,829 578,846 564,836 550,846 555,829 541,819 558,819"/>
  </g>

  <!-- Product name -->
  <text class="product-title" x="343" y="818" font-size="104" text-anchor="middle" textLength="330" lengthAdjust="spacingAndGlyphs">COPPER</text>
  <text class="product-title" x="343" y="914" font-size="104" text-anchor="middle" textLength="230" lengthAdjust="spacingAndGlyphs">TIDE</text>

  <text class="product-note" x="347" y="972" font-size="28" text-anchor="middle">NON-ALCOHOLIC</text>

  <!-- Volume badge -->
  <g class="volume-badge">
    <path d="M278 1200 V1080 L342 1035 L406 1080 V1200 Z" fill="var(--forest)"/>
    <path d="M288 1200 V1086 L342 1048 L396 1086 V1200 Z" fill="url(#volumeBadge)"/>
    <text class="volume" x="342" y="1122" font-size="34" text-anchor="middle">FULL</text>
    <text class="volume" x="342" y="1160" font-size="34" text-anchor="middle">12 OZ</text>
  </g>
</svg>
</body>
</html>
```